Business Card Design

I am a mental health counselor in private practice. I provide counseling to individuals, couples, and adults. There is a design on CardLoom that I really like. It is 2 talking bubbles joined together by a heart. That is just a suggestion. I'm interested in other ideas. I would like my photo to be on the back of the card, along with the text Miriam Delacott Counseling. I would like mint green as my background color and navy writing, if possible. The final design should be elegant, professional, and maybe just a touch whimsical.
Target Market(s)
Individual adolescents, adults, couples, and families seeking counseling.
Industry/Entity Type
Mental Health
Contact Information for Business Card
Miriam Delacott
A Wholehearted Approach to Counseling
Miriam Delacott, M.S. NCC
Wexmoor Hall
2947 NW Calloway Street, Suite 318
Portland OR 97209
503-286-1573
counselingwithmiriam-example.com
Requirements
Must have
- The card must have all of the text provided and my photo.
Nice to have
- I like cards that are rounded on the sides, and I like thick paper.

```html
<!DOCTYPE html>
<html lang="en">
<head>
<meta charset="utf-8">
<title>Miriam Delacott Counseling – Business Card</title>
<link rel="stylesheet" href="https://fonts.googleapis.com/css2?family=Josefin+Sans:wght@300;400&display=swap">
<style>
  :root {
    --page: #e9ebea;
    --mint: #45bfb3;
    --mint-edge: #34a69a;
    --navy: #3d3590;
    --cloud: #ffffff;
    --photo-top: #e8d3a8;
    --photo-bottom: #1f1f24;
  }
  html, body {
    margin: 0;
    width: 1200px;
    height: 900px;
    overflow: hidden;
    background: var(--page);
    font-family: "Josefin Sans", sans-serif;
    color: var(--navy);
  }
  .canvas {
    position: relative;
    width: 1200px;
    height: 900px;
  }
  .card {
    position: absolute;
    width: 500px;
    height: 290px;
    background: var(--mint);
    border-radius: 24px;
    box-shadow: 0 5px 0 var(--mint-edge), 0 10px 0 var(--mint-edge), 0 18px 24px rgba(0,0,0,0.15);
    overflow: hidden;
  }
  .card--front { left: 70px; top: 190px; }
  .card--back  { left: 630px; top: 420px; }

  .bubbles {
    position: absolute;
    display: block;
  }

  /* Front card */
  .card--front .tagline {
    position: absolute;
    top: 30px;
    left: 0;
    right: 0;
    text-align: center;
    font-size: 19px;
    font-weight: 300;
    letter-spacing: 0.5px;
    margin: 0;
  }
  .card--front .bubbles { left: 290px; top: 70px; width: 150px; height: 52px; }
  .portrait {
    position: absolute;
    left: 34px;
    bottom: 0;
    width: 200px;
    height: 196px;
    border-radius: 90px 90px 0 0;
    background: linear-gradient(180deg, var(--photo-top) 0%, #d9b7a0 45%, var(--photo-bottom) 75%);
  }
  .contact {
    position: absolute;
    left: 290px;
    top: 138px;
    margin: 0;
    font-style: normal;
  }
  .contact .name {
    display: block;
    font-size: 17px;
    font-weight: 300;
    margin-bottom: 4px;
  }
  .contact .address,
  .contact .phone {
    display: block;
    font-size: 13.5px;
    font-weight: 300;
    line-height: 1.3;
  }

  /* Back card */
  .card--back .bubbles { left: 172px; top: 46px; width: 156px; height: 54px; }
  .card--back .identity {
    position: absolute;
    top: 116px;
    left: 0;
    right: 0;
    text-align: center;
  }
  .card--back .name {
    margin: 0;
    font-size: 27px;
    font-weight: 400;
    letter-spacing: 1.5px;
  }
  .card--back .tagline {
    margin: 8px 0 0;
    font-size: 20px;
    font-weight: 300;
    letter-spacing: 0.5px;
  }
  .card--back .website {
    margin: 18px 0 0;
    font-size: 16px;
    font-weight: 300;
    letter-spacing: 0.5px;
  }
</style>
</head>
<body>
<main class="canvas">

  <section class="card card--front" aria-label="Card front">
    <p class="tagline">A Wholehearted Approach to Counseling</p>
    <svg class="bubbles" viewBox="0 0 150 52" role="img" aria-label="Two speech bubbles joined by a heart">
      <rect x="0" y="4" width="150" height="44" rx="22" fill="var(--cloud)"/>
    </svg>
    <div class="portrait" role="img" aria-label="Portrait photo of the counselor"></div>
    <address class="contact">
      <span class="name">Miriam Delacott M.S</span>
      <span class="address">NCC Wexmoor Hall 2947<br>NW Calloway Street,<br>Suite 318 Portland<br>OR 97209</span>
      <span class="phone">503-286-1573</span>
    </address>
  </section>

  <section class="card card--back" aria-label="Card back">
    <svg class="bubbles" viewBox="0 0 156 54" role="img" aria-label="Two speech bubbles joined by a heart">
      <rect x="0" y="4" width="156" height="46" rx="23" fill="var(--cloud)"/>
    </svg>
    <div class="identity">
      <h1 class="name">MIRIAM DELACOTT</h1>
      <p class="tagline">A Wholehearted Approach to Counseling</p>
      <p class="website">www.counselingwithmiriam-example.com</p>
    </div>
  </section>

</main>
</body>
</html>
```